The ELM Groote Eylandt - Menu 2020

I am looking for a new desgin on our menu. Preferbly 1 page but happy for it to be in A3. See attached what we are currently using which was designed by one of our admin people which is ok but is a bit busy. The ELM logo is already in use so this would need to stay as is, otherwise the layout /design /background im happy to review all. This is a beach side pub with simple fresh food.

Target Market(s)

FIFO Workforce as well as young familes residential.

Requirements
Must have
• match the logo.
Nice to have
• on 1 page (not turn over)
Should not have
• Anything not family friendly

```html
<!DOCTYPE html>
<html lang="en">
<head>
<meta charset="utf-8">
<title>The ELM – Menu</title>
<link href="https://fonts.googleapis.com/css2?family=Montserrat:wght@500;600;700&family=Oswald:wght@500;600&family=Kaushan+Script&family=Libre+Baskerville:ital@1&display=swap" rel="stylesheet">
<style>
:root{
  --bg:#e6e8ea;
  --paper:#f7f8f9;
  --blue:#2aa3dc;
  --blue-soft:#cfe9f6;
  --ink:#26313c;
  --ink-soft:#5b6873;
  --black:#141414;
}
*{box-sizing:border-box;margin:0;padding:0}
html,body{width:1200px;height:801px;overflow:hidden;background:var(--bg)}
body{position:relative;font-family:"Montserrat",sans-serif;color:var(--ink)}
.page{position:absolute;top:40px;width:510px;height:721px;background:var(--paper);box-shadow:0 4px 14px rgba(0,0,0,.15);overflow:hidden}
.cover{left:70px}
.menu{left:620px;padding:22px 20px 18px}

/* cover */
.cover-pattern{position:absolute;inset:0;background:radial-gradient(circle at 50% 50%,#e3f2fa 0%,#d2ebf7 60%,#c4e4f4 100%)}
.cover-brand{position:absolute;left:0;right:0;top:310px;text-align:center}
.brand-name{font-family:"Montserrat",sans-serif;font-weight:700;color:var(--black);font-size:26px;letter-spacing:2px;line-height:1.2;text-transform:uppercase}

/* menu page */
.cols{display:flex;gap:18px;height:100%}
.col{flex:1;display:flex;flex-direction:column}
.hours{border-top:1px solid var(--blue);border-bottom:1px solid var(--blue);padding:5px 0;margin:6px 0 10px;font-size:7.5px;font-weight:600;letter-spacing:.5px;text-align:center;color:var(--ink)}
.ribbon{background:var(--blue);color:#fff;padding:3px 10px;margin:4px 0 4px -20px;width:fit-content;clip-path:polygon(0 0,100% 0,94% 50%,100% 100%,0 100%)}
.ribbon.right{margin:4px -20px 4px auto;clip-path:polygon(0 0,100% 0,100% 100%,0 100%,6% 50%)}
.script{font-family:"Kaushan Script",cursive;font-size:15px;font-weight:400}
.band{font-family:"Oswald",sans-serif;font-size:12px;letter-spacing:1px;text-transform:uppercase}
.band small{font-size:7px}
.note{font-family:"Libre Baskerville",serif;font-style:italic;color:var(--blue);font-size:7.5px;text-align:center;margin:2px 0 5px}
.item{display:flex;justify-content:space-between;gap:6px;font-size:7.3px;font-weight:600;text-transform:uppercase;letter-spacing:.4px;margin-top:4px}
.item .price{white-space:nowrap;font-weight:500;text-align:right;line-height:1.25}
.desc{font-family:"Libre Baskerville",serif;font-style:italic;font-size:5.4px;color:var(--ink-soft);line-height:1.35;margin-top:1px}
.sub{display:flex;justify-content:space-between;font-size:7px;font-weight:500;margin-top:2px;padding-left:10px}
.section-title{font-family:"Oswald",sans-serif;color:var(--blue);font-size:11px;text-transform:uppercase;text-align:center;margin:9px 0 3px;letter-spacing:.5px}
.fillings{color:var(--blue);font-size:7px;font-weight:500;line-height:1.45;padding-left:8px}
.fillings .lead{font-family:"Libre Baskerville",serif;font-style:italic;color:var(--ink);font-size:7px}
.footnote{font-family:"Libre Baskerville",serif;font-style:italic;font-size:7px;text-align:center;margin-top:8px;color:var(--ink)}
.art{border-radius:6px;background:linear-gradient(135deg,#e9f4fa,#cfe6f2)}
.row-art{display:flex;gap:8px;align-items:flex-start}
.row-art .fillings{flex:1}

.head{text-align:center;margin:4px 0 8px}
.head .brand-name{font-size:11px;letter-spacing:1px}
.address{font-size:6.5px;font-weight:500;border-top:1px solid var(--blue);border-bottom:1px solid var(--blue);padding:4px 0;text-align:center;margin-bottom:8px;color:var(--ink)}
.mains{border:1px solid var(--blue);border-radius:6px;padding:6px 10px 8px;margin:8px 0 4px}
.mains .section-title{margin-top:0;font-size:13px}
.kids-head{display:flex;justify-content:space-between;align-items:flex-start;margin-top:8px}
.kids-title{font-family:"Kaushan Script",cursive;color:var(--blue);font-size:14px}
.kids-note{font-family:"Libre Baskerville",serif;font-style:italic;font-size:6px;color:var(--blue);text-align:right}
.kids-list{font-size:7px;font-weight:600;text-transform:uppercase;line-height:1.5;letter-spacing:.3px;margin-top:3px}
</style>
</head>
<body>

<section class="page cover">
  <div class="cover-pattern" role="img" aria-label="Light blue pattern of hand-drawn nautical motifs: ships, anchors, ship wheels, lighthouses, seagulls, shells and life rings"></div>
  <div class="cover-brand">
    <div class="brand-name">Kurrabay<br>The ELM<br>Recreation Club</div>
  </div>
</section>

<section class="page menu">
  <div class="cols">
    <div class="col">
      <div class="hours">LUNCH: 12.00pm - 2.00pm<br>DINNER: 5.30pm - 8.30pm</div>

      <div class="ribbon script">All Day Bar Menu</div>
      <div class="note">★ Available: 11:30am - 8:30pm ★</div>

      <div class="item"><span>Crispy Chicken Wings</span><span class="price">5 Wings $7.5<br>10 Wings $15.0</span></div>
      <div class="desc">Your Choice of Sauce (Ranch, Spicy Buffalo, BBQ or South West Sauce)</div>
      <div class="item"><span>Trio of Sliders</span><span class="price">$12.0</span></div>
      <div class="desc">Smoky Pulled Pork, South West Pulled Beef Brisket and Southern Fried Chicken with Sriracha Mayo. All served with Fresh Slaw.</div>
      <div class="item"><span>Vege Fries</span><span class="price">(V) $8.0</span></div>
      <div class="desc">Parsnip, Beets &amp; Carrot Fries with Rosemary Sea Salt and Chipotle Mayo</div>
      <div class="item"><span>Crispy Fries</span><span class="price">$6.0<br>$9.0</span></div>
      <div class="desc">Plain Fries<br>With Gravy, Shaved Gouda Cheese &amp; Grilled Bacon</div>
      <div class="item"><span>Garlic Bread</span><span class="price">$4.0</span></div>
      <div class="item"><span>Cheesy Garlic Bread</span><span class="price">$5.0</span></div>

      <div class="section-title">Tacos, Nachos or Quesadillas</div>
      <div class="item"><span>Tacos</span><span class="price">$16.0</span></div>
      <div class="desc">Soft Tortilla with Your Choice of Filling, Fresh Slaw, Avocado, Sriracha Cream &amp; Lime Wedge</div>
      <div class="item"><span>Nachos</span><span class="price">$18.0</span></div>
      <div class="desc">Toasted Corn Chips Topped with Your Choice of Filling, Avocado, Fresh Tomato Salsa, Melted Cheese, Sour Cream &amp; Jalapenos</div>
      <div class="item"><span>Quesadillas</span><span class="price">$16.0</span></div>
      <div class="desc">Toasted Tortilla with Your Choice of Filling, Baby Spinach, Roasted Red Pepper, Gouda &amp; Buffalo Mozzarella</div>

      <div class="row-art" style="margin-top:5px">
        <div class="fillings">
          <div class="lead">★ Choose Your Filling From The Below</div>
          Smokey BBQ Pulled Pork<br>Southern Fried Chicken<br>South West Pulled Beef Brisket<br>Chilli Black Bean<br>Grilled Cajun Prawns ..... $6.0
        </div>
        <div class="art" style="width:52px;height:60px" role="img" aria-label="Sketch of a taco and a burger"></div>
      </div>

      <div class="ribbon band">Burger <small>and</small> Salads</div>
      <div class="note">All burgers served with steak chips</div>
      <div class="item"><span>Pulled Pork Burger</span><span class="price">$22.0</span></div>
      <div class="desc">Pulled Pork, Fresh Slaw, Pickles &amp; Spicy BBQ Sauce On A Brioche Bun</div>
      <div class="item"><span>Beef, Bacon &amp; Cheese Burger</span><span class="price">$22.0</span></div>
      <div class="desc">Beef Patty, Maple Bacon, Cheddar Cheese, Tomato, Cos Lettuce, Caramelised Onion &amp; Smoky BBQ Sauce On A Seeded Bun</div>
      <div class="item"><span>Southern Fried Chicken Burger<br>(*Grilled Chicken Available)</span><span class="price">$22.0</span></div>
      <div class="desc">Chicken Breast, Sliced Swiss Cheese, Baby Spinach &amp; Sriracha Mayo On A Brioche Bun</div>
      <div class="footnote">★ Ask for Vegetarian Substitutes &amp;<br>All Options Can Be Served Bunless ★</div>
    </div>

    <div class="col">
      <div class="head">
        <div class="brand-name">Kurrabay The ELM<br>Recreation Club</div>
      </div>
      <div class="address">Tidewater Drive, Kurrabay<br>Northern Territory, Australia</div>

      <div class="item"><span>Caesar Salad</span><span class="price">$18.0</span></div>
      <div class="desc">Cos Lettuce, Crispy Garlic Croutons, Bacon, Shaved Parmesan, Free Range Egg, Caesar Dressing &amp; Anchovies</div>
      <div class="sub"><span>Add Grilled Chicken</span><span>$4.0</span></div>
      <div class="sub"><span>Add Grilled Prawns</span><span>$5.0</span></div>
      <div class="item"><span>Leaf Eater Salad</span><span class="price">$18.0</span></div>
      <div class="desc">Baby Spinach, Mixed Green Leaves, Avocado, Roasted Red Peppers, Buffalo Mozzarella, Baked Tortilla Strips Served with A Balsamic Reduction</div>
      <div class="sub"><span>Add Grilled Chicken</span><span>$4.0</span></div>
      <div class="sub"><span>Add Grilled Prawns</span><span>$5.0</span></div>

      <div class="mains">
        <div class="section-title">– Mains –</div>
        <div class="note" style="margin-top:0">All meals served with 2 sides</div>
        <div class="item"><span>Sticky BBQ Pork Ribs ½ Rack</span><span class="price">$35.0</span></div>
        <div class="item"><span>Battered Fish and Chips</span><span class="price">$24.0</span></div>
        <div class="item"><span>Chicken Schnitzel</span><span class="price">$25.0</span></div>
        <div class="item"><span>Chicken Parmigiana</span><span class="price">$28.0</span></div>
        <div class="item"><span>400g Rib Fillet on the Bone</span><span class="price">$42.0</span></div>
        <div class="item"><span>300g Scotch Fillet</span><span class="price">$35.0</span></div>
        <div class="item"><span>400g Wagyu Rump</span><span class="price">$35.0</span></div>
      </div>

      <div class="ribbon right band">Sides <small>and</small> Sauces</div>
      <div class="row-art">
        <div class="art" style="width:46px;height:30px" role="img" aria-label="Sketch of a bowl of salad"></div>
        <div style="flex:1">
          <div class="item" style="margin-top:0"><span>Side #1</span></div>
          <div class="desc">Creamy Mashed Potato or Seasoned Steak Chips</div>
        </div>
      </div>
      <div class="item"><span>Side #2</span></div>
      <div class="desc">Green Salad, Fresh Slaw, Seasonal Vegetables or Mini Caesar Salad</div>
      <div class="item" style="text-transform:none;font-weight:500"><span>Char Grilled Cajun Corn on the Cob</span><span class="price">$5.0</span></div>
      <div class="item" style="text-transform:none;font-weight:500"><span>Creamy Mushroom - Peppercorn Sauce<br>Traditional Gravy - Smoky BBQ Sauce<br>Bearnaise Sauce</span><span class="price">$2.0</span></div>
      <div class="item" style="text-transform:none;font-weight:500"><span>Extra Sauces</span><span class="price">$1.5</span></div>

      <div class="kids-head">
        <div class="kids-title">Kids Menu</div>
        <div class="kids-note">★ All Kids Meals $9<br>with a Paper Cup of<br>Ice Cream &amp; Topping ★</div>
      </div>
      <div class="row-art">
        <div class="kids-list" style="flex:1">
          Steak with Chips &amp; Veg<br>Cheeseburger &amp; Fries<br>Grilled Chicken Burger with<br>Cheese, Lettuce, Mayo &amp; Fries<br>Spaghetti Bolognaise<br>Fish and Chips<br>Mini Southern Fried<br>Chicken Bites &amp; Chips
        </div>
        <div class="art" style="width:50px;height:56px;margin-top:10px" role="img" aria-label="Sketch of a cup of fries"></div>
      </div>
    </div>
  </div>
</section>

</body>
</html>
```